BRIGHTWAVE DENTAL *

please see attached.

Target Market(s)

Adults 18-60

Contact Information for Business Card

Website: brightwavedentalqz.com
Phone number 555 304 7726 email: brightwavedentalqz@mailvex.com
Address:417 S. Kellim rd
Suite#24, TX70000
Dr. Elias Varno, DDS

Font styles to use
Sans Serif

Requirements
Must have
• Logo, phone number website, doctor,
• 's name

```html
<!DOCTYPE html>
<html lang="en">
<head>
<meta charset="utf-8">
<title>Brightwave Dental – Business Card</title>
<link rel="stylesheet" href="https://fonts.googleapis.com/css2?family=Poppins:wght@300;400;600&display=swap">
<style>
  :root {
    --bg: #c8dbe8;
    --card: #ffffff;
    --card-tint: #eef0f3;
    --teal: #0f7b91;
    --charcoal: #444144;
    --ink: #3b3a3d;
  }
  * { margin: 0; padding: 0; box-sizing: border-box; }
  html, body { width: 1200px; height: 900px; overflow: hidden; }
  body {
    background: var(--bg);
    font-family: "Poppins", Arial, sans-serif;
    color: var(--ink);
    position: relative;
  }
  .card {
    position: absolute;
    left: 285px;
    width: 630px;
    height: 360px;
    background: var(--card);
    box-shadow: 0 6px 18px rgba(40, 70, 95, 0.18);
    overflow: hidden;
  }
  .card--back { top: 60px; }
  .card--front {
    top: 480px;
    background: linear-gradient(180deg, #f6f7f9 0%, var(--card-tint) 100%);
  }
  .edge-strip {
    position: absolute;
    top: 0; right: 0;
    width: 20px; height: 100%;
    background: var(--teal);
  }
  .brand {
    position: absolute;
    left: 70px; top: 152px;
    display: flex; align-items: center; gap: 14px;
    white-space: nowrap;
  }
  .brand-dot {
    width: 56px; height: 56px;
    border-radius: 50%;
    border: 2px solid var(--ink);
    flex: none;
  }
  .brand-name {
    font-weight: 300;
    font-size: 36px;
    letter-spacing: 1.5px;
    color: var(--ink);
  }
  .band {
    position: absolute;
    top: 0; left: 460px;
    width: 132px; height: 100%;
    background: var(--charcoal);
  }
  .front-art { position: absolute; inset: 0; }
  .doctor {
    position: absolute;
    left: 36px; top: 66px;
    font-size: 22px;
    font-weight: 600;
    color: var(--ink);
  }
  .doctor-name { color: var(--teal); }
  .contacts {
    position: absolute;
    left: 36px; top: 206px;
    list-style: none;
    display: flex; flex-direction: column; gap: 14px;
  }
  .contact {
    display: flex; align-items: center; gap: 12px;
    font-size: 15px;
    color: var(--ink);
  }
  .contact-icon { width: 26px; height: 26px; flex: none; }
</style>
</head>
<body>

<section class="card card--back" aria-label="Card back">
  <div class="brand">
    <span class="brand-dot"></span>
    <span class="brand-name">BRIGHTWAVE DENTAL</span>
  </div>
  <div class="edge-strip"></div>
</section>

<section class="card card--front" aria-label="Card front">
  <div class="band"></div>
  <div class="edge-strip"></div>
  <svg class="front-art" width="630" height="360" viewBox="0 0 630 360">
    <path d="M0 176 H441 A72 72 0 0 1 398 110" fill="none" stroke="#0f7b91" stroke-width="2"/>
    <circle cx="470" cy="110" r="60" fill="#ffffff"/>
    <circle cx="470" cy="110" r="50" fill="none" stroke="#444144" stroke-width="1.5"/>
  </svg>

  <p class="doctor"><span class="doctor-name">Dr. Elias Varno</span>, DDS</p>

  <ul class="contacts">
    <li class="contact">
      <svg class="contact-icon" viewBox="0 0 26 26">
        <circle cx="13" cy="13" r="11.5" fill="#fff" stroke="#0f7b91" stroke-width="2"/>
        <path d="M8 10.5c0-1.2 2.3-2 5-2s5 .8 5 2v1h-2.5v-1h-5v1H8z M9.5 12.5h7l1 5h-9z" fill="#444144"/>
      </svg>
      <span>555 304 7726</span>
    </li>
    <li class="contact">
      <svg class="contact-icon" viewBox="0 0 26 26">
        <circle cx="13" cy="13" r="11.5" fill="#fff" stroke="#0f7b91" stroke-width="2"/>
        <rect x="7.5" y="9" width="11" height="8" fill="#444144"/>
        <path d="M7.5 9 L13 13.5 L18.5 9" fill="none" stroke="#fff" stroke-width="1"/>
      </svg>
      <span>email@brightwavedentalqz.com</span>
    </li>
    <li class="contact">
      <svg class="contact-icon" viewBox="0 0 26 26">
        <circle cx="13" cy="13" r="11.5" fill="#fff" stroke="#0f7b91" stroke-width="2"/>
        <circle cx="13" cy="13" r="5.5" fill="none" stroke="#444144" stroke-width="1.3"/>
        <path d="M7.5 13h11 M13 7.5v11 M13 7.5c-2.5 2.5-2.5 8.5 0 11 M13 7.5c2.5 2.5 2.5 8.5 0 11" fill="none" stroke="#444144" stroke-width="1"/>
      </svg>
      <span>www.brightwavedentalqz.com</span>
    </li>
  </ul>
</section>

</body>
</html>
```